Attorney At Law Card Design

I am an attorney. I need something simple but elegant with nice conservative colors. The design should communicate competence, and confidence. I specialize in Personal Injury and Criminal Defense Work.

Industry/Entity Type

Conservative

Contact Information for Business Card

Velandro Law Firm
2837 Birchwell Ave.
Dunmore, TX 78611

Rodolfo "Rudy" Velandro
956-413-2716 Tel.
956-413-2719 Fax
956-582-4130 Cell

Justice for All

```html
<!DOCTYPE html>
<html lang="en">
<head>
<meta charset="utf-8">
<title>Velandro Law Firm – Business Card</title>
<link rel="stylesheet" href="https://fonts.googleapis.com/css2?family=Tinos:wght@400;700&family=Courier+Prime&display=swap">
<style>
  :root {
    --backdrop: #2a2724;
    --card-black: #000000;
    --band-blue-dark: #0f2a86;
    --band-blue: #2a4fc4;
    --band-blue-light: #5a7be0;
    --ink-white: #ffffff;
    --ink-soft: #e6e9f2;
  }
  * { margin: 0; padding: 0; box-sizing: border-box; }
  html, body {
    width: 1200px; height: 805px; overflow: hidden;
    background: var(--backdrop);
  }
  .canvas {
    position: relative; width: 1200px; height: 805px;
    display: flex; align-items: center; justify-content: center;
  }
  .card {
    position: relative; width: 1000px; height: 560px;
    background: var(--card-black);
    font-family: "Tinos", "Times New Roman", serif;
    color: var(--ink-white);
    overflow: hidden;
  }
  .brand-mark {
    position: absolute; top: 120px; left: 0; width: 100%;
    display: flex; align-items: center; justify-content: center; gap: 18px;
  }
  .brand-mark__dot {
    width: 40px; height: 40px; border-radius: 50%; background: var(--ink-white);
  }
  .brand-mark__name {
    font-size: 40px; font-weight: 400; letter-spacing: 2px; color: var(--ink-white);
  }
  .firm-name {
    position: absolute; top: 262px; left: 0; width: 100%;
    text-align: center; font-size: 70px; font-weight: 400;
    transform: scaleX(0.88);
  }
  .practice {
    position: absolute; top: 352px; left: 0; width: 100%;
    text-align: center; font-size: 27px; font-weight: 700; color: var(--ink-soft);
  }
  .attorney {
    position: absolute; top: 388px; left: 0; width: 100%;
    text-align: center; font-size: 27px; font-weight: 700; color: var(--ink-soft);
  }
  .contact-band {
    position: absolute; left: 0; right: 0; top: 430px; height: 110px;
    background: linear-gradient(100deg, var(--band-blue-dark) 0%, var(--band-blue) 45%, var(--band-blue-light) 55%, var(--band-blue) 65%, var(--band-blue-dark) 100%);
  }
  .address {
    position: absolute; left: 22px; top: 42px;
    font-size: 24px; line-height: 30px; color: var(--ink-white);
  }
  .phones {
    position: absolute; right: 26px; top: 4px;
    font-size: 24px; line-height: 26px; color: var(--ink-white);
    display: grid; grid-template-columns: auto auto; column-gap: 14px;
  }
  .phones .label { text-align: right; }
  .tagline {
    position: absolute; right: 26px; top: 58px;
    font-family: "Courier Prime", "Courier New", monospace;
    font-size: 17px; color: var(--ink-white);
  }
</style>
</head>
<body>
<main class="canvas">
  <section class="card">
    <div class="brand-mark">
      <span class="brand-mark__dot"></span>
      <span class="brand-mark__name">Velandro</span>
    </div>
    <h1 class="firm-name">Velandro Law Firm</h1>
    <p class="practice">Personal Injury and Criminal Defense</p>
    <p class="attorney">Rodolfo "Rudy" Velandro</p>
    <div class="contact-band">
      <p class="address">Velandro Law Firm 2837 Birchwell Ave. Dunmore,<br>TX 78611 Rodolfo "Rudy" Velandro 956-413-2716</p>
      <div class="phones">
        <span class="label">Cell.</span><span>956-582-4130</span>
        <span class="label">Fax.</span><span>956-413-2719</span>
      </div>
      <p class="tagline">Call Steady Counsel</p>
    </div>
  </section>
</main>
</body>
</html>
```